Business Card design for Property Developer

We need a business card design for a Melbourne based Property Developer called "Kestrel Grove Pty Ltd".

We subdivide land and onsell to builders etc.

We already have a company logo, which is attached. Also I have attached the layout requirements from the printer. We would like a 2-sided design with one side displaying our logo by itself and the other with the required info, such as name, address, tel no., email, abn etc. The card will need to be used by 4 members of staff so name and contact details should be interchangable.
Updates

If possible, can you please write "name' "job position" "phone" "email" "address" on the card but leave them so I can add the details at a later time. Thank you. Also I plan on printing with UV spot printing as a background on the card. Keep this is mind when designing.

Thanks again.

Hello designers, please do not include pics of houses, house plansĀ or construction machinery etc as we really do not like the way it looks. Thank you.

Target Market(s)

Real Estate Agents, Land Owners, Local Council Departments, Govt Bodies, other Developers etc.

Industry/Entity Type

Business

Requirements
Must have
• 2-sided design with one side displaying our logo by itself and the other with the required info, such as name, address, tel no., email, abn etc.

```html
<!DOCTYPE html>
<html lang="en">
<head>
<meta charset="utf-8">
<title>Kestrel Grove Business Card</title>
<link href="https://fonts.googleapis.com/css2?family=Michroma&family=Open+Sans:wght@400&display=swap" rel="stylesheet">
<style>
  :root {
    --page-bg: #efefef;
    --card-bg: #ffffff;
    --brand-red: #d3222a;
    --band-red: #ee2a2e;
    --band-dark: #9c1a1e;
    --navy: #1f3a8a;
    --sky: #2ab3e6;
    --brand-blue: #2c63c4;
    --faint-mark: #e4eaf1;
  }
  * { margin: 0; padding: 0; box-sizing: border-box; }
  html, body {
    width: 1200px;
    height: 900px;
    overflow: hidden;
    background: var(--page-bg);
  }
  .card {
    position: absolute;
    left: 310px;
    width: 560px;
    height: 336px;
    background: var(--card-bg);
    overflow: hidden;
  }
  .card--front { top: 60px; }
  .card--back { top: 510px; }

  .brand-lockup {
    position: absolute;
    left: 0;
    right: 0;
    top: 68px;
    display: flex;
    flex-direction: column;
    align-items: center;
    gap: 22px;
  }
  .brand-dot {
    width: 130px;
    height: 130px;
    border-radius: 50%;
    background: var(--brand-blue);
  }
  .brand-name {
    font-family: "Michroma", sans-serif;
    font-size: 30px;
    color: var(--brand-red);
    letter-spacing: 1px;
  }

  .edge-band {
    position: absolute;
    left: 0;
    top: 0;
    width: 40px;
    height: 100%;
    background: var(--band-red);
  }
  .edge-band::before {
    content: "";
    position: absolute;
    left: 0;
    top: 0;
    width: 16px;
    height: 100%;
    background: var(--band-dark);
  }
  .faint-name {
    position: absolute;
    left: 372px;
    top: 128px;
    font-family: "Michroma", sans-serif;
    font-size: 26px;
    line-height: 1.35;
    color: var(--faint-mark);
  }

  .details {
    position: absolute;
    left: 64px;
    top: 42px;
  }
  .person-name {
    font-family: "Michroma", sans-serif;
    font-size: 21px;
    font-weight: 400;
    color: var(--navy);
    line-height: 1.2;
  }
  .person-role, .company-address {
    font-family: "Open Sans", sans-serif;
    font-size: 19px;
    color: var(--sky);
    line-height: 1.2;
  }
  .company-name {
    margin-top: 22px;
    font-family: "Michroma", sans-serif;
    font-size: 16px;
    color: var(--navy);
    line-height: 1.3;
  }

  .contact-list {
    position: absolute;
    left: 64px;
    top: 240px;
    list-style: none;
    font-family: "Open Sans", sans-serif;
    font-size: 18px;
    color: var(--sky);
  }
  .contact-list li {
    display: flex;
    align-items: center;
    gap: 12px;
    height: 34px;
  }
  .contact-list .contact-email { font-size: 16px; }
  .contact-icon { width: 18px; height: 16px; flex: none; }
</style>
</head>
<body>
  <section class="card card--front" aria-label="Card front">
    <div class="brand-lockup">
      <div class="brand-dot" aria-hidden="true"></div>
      <div class="brand-name">KESTREL GROVE</div>
    </div>
  </section>

  <section class="card card--back" aria-label="Card back">
    <div class="edge-band" aria-hidden="true"></div>
    <div class="faint-name" aria-hidden="true">KESTREL<br>GROVE</div>

    <div class="details">
      <h1 class="person-name">DANIEL REYES</h1>
      <p class="person-role">manager</p>
      <p class="company-name">KESTREL GROVE</p>
      <p class="company-address">Address</p>
    </div>

    <ul class="contact-list">
      <li>
        <svg class="contact-icon" viewBox="0 0 18 16" aria-hidden="true">
          <path d="M1 5 Q9 -1 17 5 L15 7 L12 5.5 L12 4 Q9 3 6 4 L6 5.5 L3 7 Z" fill="#1f3a8a"/>
          <rect x="3" y="8" width="12" height="7" rx="1.5" fill="#1f3a8a"/>
          <circle cx="9" cy="11.5" r="1.8" fill="#ffffff"/>
        </svg>
        <span>0398765432</span>
      </li>
      <li class="contact-email">
        <svg class="contact-icon" viewBox="0 0 18 16" aria-hidden="true">
          <rect x="1" y="2" width="16" height="12" fill="none" stroke="#1f3a8a" stroke-width="2"/>
          <path d="M1 2 L9 9 L17 2" fill="none" stroke="#1f3a8a" stroke-width="2"/>
        </svg>
        <span>daniel.reyes@kestrelgrove.com</span>
      </li>
    </ul>
  </section>
</body>
</html>
```